POP/ROCK artist: CD Cover Design Project

IF U LOVE MUSIC AND ALBUM COVER ART THEN PLEASE PARTICIPATE IN MY PROJECT AND HAVE A GREAT TIME DESIGNING SOMETHING UNIQUE AND EXCITING!!!!
Hi, my name is tovo, a pop/rock artist living in Europe. i just finished recording a fun dance song, called SPINNIN WILD HEARTS, with a successful Brightfield Records producer in Europe and I just put the finishing touches on the music video shot in LA. Now i'm going to release the song and video with PulsaWave. It's going to go out to about 750 stores, including SongCrate, tunebox and all the other biggies as well as a load of smaller ones.
I need a great looking CD cover design that i can plaster everywhere . . . and i really mean everywhere i can.
As per PulsaWave' specs, the cover art MUST BE 1500 x 1500 pixels. It cannot be blurry or pixilated and must be perfectly square.
I've uploaded some pics for you to choose from but you can use whichever one(s) you like . . . or none of them if you prefer, according to your inspiration. Just let me know if you want other pics and i can upload others.
Updates
Hey there,
Hey there,
Hi again, all,
Hey there,
Hi there, designers!
Hello everybody,
Target Market(s)
Modern pop/rock radio listeners of Kestrel Radio, ZPX, etc.
Please click on the following link to see the music video and hear the song:
http://www.clipvault.example/watch?v=Qr7tLm2Wd9a
Also, i have various pics and photos i can upload . . . just tell me what you need!!!!!
Requirements
Must have
- As per PulsaWave' specs, the cover art MUST BE 1500 x 1500 pixels. It cannot be blurry or pixilated and must be perfectly square.
My artist name, tovo, and the song title, Spinnin Wild Hearts, must be on the cover art.
The destination for your design is online music stores like SongCrate. So the dimensions will be VERY SMALL The actual size seen by the public will be about 1.5 cm x 1.5 cm! (Please have a look at the SongCrate store to see the actual size people will view the designs in.)
This means that your designs have to be clearly communicated at that size. The title of the song (spinnin wild hearts) and my artist name (tovo) have to be large enough to read and whatever idea you're going for has to be easily understood.
Nice to have
- It should look totally modern and pop/rock, hip and cool. It's up to you and your design magic to do whatever you think it takes.
Should not have
- Website and e-mail addresses CANNOT be included anywhere on cover art.

```html
<!DOCTYPE html>
<html lang="en">
<head>
<meta charset="utf-8">
<title>tovo – Spinnin Wild Hearts</title>
<link rel="stylesheet" href="https://fonts.googleapis.com/css2?family=Archivo+Black&family=Arimo:wght@700&display=swap">
<style>
  :root {
    --night: #07080d;
    --night-deep: #020306;
    --moon-light: #f6cf86;
    --moon-mid: #e6a64f;
    --moon-edge: #b8772e;
    --halo: rgba(255, 255, 255, 0.9);
    --type: #ffffff;
    --type-glow: rgba(190, 205, 255, 0.85);
    --silhouette: #0b0b0b;
  }
  * { margin: 0; padding: 0; box-sizing: border-box; }
  html, body {
    width: 1200px;
    height: 1200px;
    overflow: hidden;
    background: var(--night-deep);
  }
  .cover {
    position: relative;
    width: 1200px;
    height: 1200px;
    overflow: hidden;
  }
  .night-sky {
    position: absolute;
    inset: 0;
    background: radial-gradient(ellipse at 60% 45%, #12141d 0%, var(--night) 55%, var(--night-deep) 100%);
  }
  .moon {
    position: absolute;
    left: 540px;
    top: 120px;
    width: 488px;
    height: 488px;
    border-radius: 50%;
    background: radial-gradient(circle at 45% 42%, var(--moon-light) 0%, var(--moon-mid) 60%, var(--moon-edge) 100%);
    box-shadow: 0 0 14px 6px var(--halo), 0 0 40px 10px rgba(255, 255, 255, 0.35);
  }
  .artist-name {
    position: absolute;
    left: 0;
    right: 0;
    top: 640px;
    text-align: center;
    font-family: "Archivo Black", "Arial Black", sans-serif;
    font-size: 224px;
    line-height: 1;
    letter-spacing: 22px;
    padding-left: 22px;
    color: var(--type);
    text-shadow: 0 0 18px var(--type-glow), 0 0 40px rgba(255, 255, 255, 0.55);
  }
  .song-title {
    position: absolute;
    left: 0;
    right: 0;
    top: 906px;
    text-align: center;
    font-family: "Arimo", Arial, sans-serif;
    font-weight: 700;
    font-size: 94px;
    line-height: 104px;
    letter-spacing: 6px;
    color: var(--type);
  }
  .song-title span { display: block; }
</style>
</head>
<body>
  <main class="cover">
    <div class="night-sky" role="img" aria-label="Photograph of a dark night sky scattered with faint stars"></div>
    <div class="moon" role="img" aria-label="Photograph of a glowing orange full moon with the silhouette of a convertible car flying across it"></div>
    <h1 class="artist-name">TOVO</h1>
    <h2 class="song-title">
      <span>SPINNIN</span>
      <span>WILD HEARTS</span>
    </h2>
  </main>
</body>
</html>
```